Copper and Slate Mists NZ new website!

We are a new online vaping retailer and are looking for an awesome sleek website. We are going to be selling a variety of vaping products and gear. Our logo has just been developed and we would like to keep the website in line with the black, tan a white theme. We would like to trying watermarking or imposing the rottie into the background of the website on the home page, with the page being black and you can see the tan and white colours only.

Coding

Coded - Design and coding required

Number of Pages Required

2 page

Font styles to use
Serif
Sans Serif
Decorative

Requirements
Must have
• A home page and a standard page for products
• Stay in line with the colours in the logo

```html
<!DOCTYPE html>
<html lang="en">
<head>
<meta charset="utf-8">
<title>Copper and Slate Mists NZ</title>
<link rel="stylesheet" href="https://fonts.googleapis.com/css2?family=Raleway:wght@400;500;600;700&family=Oswald:wght@500&display=swap">
<style>
:root{
  --tan:#b8661a;
  --tan-light:#c9772a;
  --ink:#0a0a0a;
  --night:#1f1d1c;
  --slate:#3e3e3e;
  --white:#ffffff;
  --muted:#9a9a9a;
  --field:#f2f2f2;
}
*{box-sizing:border-box;margin:0;padding:0}
html,body{width:706px;height:1200px;overflow:hidden;background:var(--night)}
body{position:relative;font-family:"Raleway",Arial,sans-serif;color:var(--white)}
.abs{position:absolute}
.backdrop{left:0;top:0;width:706px;height:946px;
  background:radial-gradient(ellipse at 38% 58%,#4a3a2c 0%,#2b2520 38%,#1c1a19 70%)}
.topbar{left:0;top:0;width:706px;height:20px;background:rgba(0,0,0,.55);border-bottom:1px solid rgba(255,255,255,.12);
  font-family:"Oswald",sans-serif;font-size:8px;letter-spacing:.3px}
.topbar .shipping{left:75px;top:5px;display:flex;align-items:center;gap:6px}
.topbar .phone{right:66px;top:5px;display:flex;align-items:center;gap:6px}
.search{left:67px;top:40px;width:162px;height:21px;display:flex}
.search .field{flex:1;background:var(--ink);border:1px solid #777;font-size:7px;padding:6px 5px;font-weight:600}
.search .go{width:22px;background:#bdbdbd;display:flex;align-items:center;justify-content:center}
.brand{left:283px;top:41px;width:142px;text-align:center;font-size:9px;font-weight:700;color:var(--white);letter-spacing:.4px;line-height:1.25}
.account{top:44px;display:flex;align-items:center;gap:6px;font-size:7px;font-weight:600}
.nav{left:67px;top:76px;width:573px;height:27px;background:var(--ink);display:flex;justify-content:center;gap:16px;font-size:7.5px;font-weight:700}
.nav a{color:var(--white);text-decoration:none;padding-top:10px}
.nav a.current{color:var(--tan-light);border-bottom:2px solid var(--tan-light)}
.hero-visual{left:76px;top:135px;width:269px;height:144px;background:linear-gradient(180deg,#f7f7f7,#d8d8d8)}
.hero-copy{right:145px;top:166px;text-align:right}
.hero-copy .kicker{font-size:14px;font-weight:500;letter-spacing:.3px}
.hero-copy .headline{font-size:29px;font-weight:600;color:var(--tan-light);margin-top:5px;letter-spacing:.3px}
.btn-grey{display:inline-block;background:#8a8a8a;color:var(--white);font-size:8px;font-weight:700;padding:4px 8px;margin-top:6px}
.rule{left:0;width:706px;height:1px;background:rgba(255,255,255,.2)}
.section-title{left:0;width:706px;text-align:center;font-size:17px;font-weight:700;letter-spacing:.2px}
.category{width:150px;text-align:center}
.category h3{font-size:17px;font-weight:600;color:var(--tan-light);letter-spacing:.2px}
.category p{font-size:8.4px;font-weight:700;line-height:16.5px;margin-top:1px}
.btn-tan{background:var(--tan);color:var(--white);font-weight:700;text-align:center;display:flex;align-items:center;justify-content:center}
.card{top:639px;height:211px;border:5px solid var(--tan);background:rgba(10,10,10,.45);text-align:center}
.card .item{position:absolute;left:50%;top:6px;width:30px;height:125px;margin-left:-15px;background:linear-gradient(90deg,#7d7d7d,#f1f1f1 45%,#9a9a9a)}
.card .price{position:absolute;left:0;right:0;top:135px;font-size:16px;font-weight:700}
.card .pname{position:absolute;left:0;right:0;top:158px;font-size:10px;font-weight:600}
.card .add{position:absolute;left:-5px;right:-5px;bottom:-5px;height:22px;background:var(--tan);font-size:7.5px;font-weight:700;padding-top:8px}
.footer{left:0;top:946px;width:706px;height:222px;background:var(--slate)}
.follow{left:62px;top:985px}
.follow h4{font-size:9.5px;font-weight:700}
.follow p{font-size:7.4px;color:var(--muted);margin-top:5px}
.subscribe{left:356px;top:985px;width:280px;height:24px;display:flex}
.subscribe .field{flex:1;background:var(--field);color:#999;font-size:6.5px;padding:9px 9px}
.subscribe .send{width:88px;background:var(--ink);font-size:8px;font-weight:700;display:flex;align-items:center;justify-content:center}
.links{top:1047px}
.links h5{font-size:10px;font-weight:500;letter-spacing:.2px;margin-bottom:7px}
.links li{list-style:none;font-size:7.6px;color:var(--muted);line-height:15px}
.bottom{left:0;top:1168px;width:706px;height:32px;background:var(--ink)}
.social{left:64px;top:13px;display:flex;gap:14px}
.social span{width:5px;height:5px;border-radius:50%;background:#999}
.copyright{left:0;width:706px;top:12px;text-align:center;font-family:"Oswald",sans-serif;font-size:5.5px;letter-spacing:.2px}
.payments{left:526px;top:11px;display:flex;gap:6px}
.payments span{width:17px;height:10px;background:#bdbdbd;border-radius:1px}
</style>
</head>
<body>
<div class="abs backdrop" role="img" aria-label="Dark photograph of a rottweiler resting on a wooden porch, tinted black with tan and white tones"></div>

<header>
  <div class="abs topbar">
    <div class="abs shipping">
      <svg width="13" height="9" viewBox="0 0 13 9"><rect x="0" y="1" width="8" height="6" fill="#fff"/><path d="M8 3h3l2 2v2H8z" fill="#fff"/><circle cx="3" cy="8" r="1.2" fill="#fff"/><circle cx="10" cy="8" r="1.2" fill="#fff"/></svg>
      <span>FREE SHIPPING</span>
    </div>
    <div class="abs phone">
      <svg width="10" height="10" viewBox="0 0 10 10"><path d="M2 0.5l2 2-1 1.3a6 6 0 0 0 3.2 3.2l1.3-1 2 2-1.2 1.5C5 9.5 0.5 5 0.5 1.7z" fill="#fff"/></svg>
      <span>+64 9876 5432 10</span>
    </div>
  </div>

  <div class="abs search">
    <div class="field">Serch here...</div>
    <div class="go"><svg width="11" height="11" viewBox="0 0 11 11"><circle cx="4.5" cy="4.5" r="3.2" fill="none" stroke="#b8661a" stroke-width="1.6"/><path d="M7 7l3.3 3.3" stroke="#b8661a" stroke-width="1.8"/></svg></div>
  </div>

  <div class="abs brand">COPPER AND SLATE<br>MISTS NZ</div>

  <div class="abs account" style="left:490px">
    <svg width="16" height="15" viewBox="0 0 16 15"><path d="M8 14.5C3 10.5 0.5 8 0.5 4.6 0.5 2.3 2.3 0.5 4.5 0.5 6 0.5 7.3 1.4 8 2.6 8.7 1.4 10 0.5 11.5 0.5 13.7 0.5 15.5 2.3 15.5 4.6 15.5 8 13 10.5 8 14.5z" fill="#ccc"/></svg>
    <span>WISHLIST</span>
  </div>
  <div class="abs account" style="left:570px">
    <svg width="18" height="15" viewBox="0 0 18 15"><path d="M0.5 1h3l2 9h10l1.5-6.5H5" fill="none" stroke="#ccc" stroke-width="1.2"/><circle cx="7" cy="13" r="1.3" fill="#ccc"/><circle cx="14" cy="13" r="1.3" fill="#ccc"/></svg>
    <span>MY CART</span>
  </div>

  <nav class="abs nav">
    <a class="current">HOME</a><a>ABOUT</a><a>PRODUCTS</a><a>CONTACT US</a><a>SHOP</a>
  </nav>
</header>

<section class="hero">
  <div class="abs hero-visual" role="img" aria-label="Row of vape pens and mods with coloured tanks on white"></div>
  <div class="abs hero-copy">
    <div class="kicker">QUIT SMOKING</div>
    <div class="headline">LET’S VAPING</div>
    <span class="btn-grey">SHOP NOW</span>
  </div>
</section>

<div class="abs rule" style="top:328px"></div>

<section class="categories">
  <h2 class="abs section-title" style="top:381px">PRODUCT CATEGORIES</h2>
  <div class="abs category" style="left:62px;top:422px"><h3>E-JUICES</h3><p>LOREM IPSUM DOLOR SIT<br>AMET, CONECTETUER<br>ADIPISCING ELIT. PRAESENT</p></div>
  <div class="abs category" style="left:209px;top:422px"><h3>DEVICES</h3><p>LOREM IPSUM DOLOR SIT<br>AMET, CONECTETUER<br>ADIPISCING ELIT. PRAESENT</p></div>
  <div class="abs category" style="left:363px;top:423px"><h3>ACCESSOIRES</h3><p>LOREM IPSUM DOLOR SIT<br>AMET, CONECTETUER<br>ADIPISCING ELIT. PRAESENT</p></div>
  <div class="abs category" style="left:506px;top:421px"><h3>STARTER KITS</h3><p>LOREM IPSUM DOLOR SIT<br>AMET, CONECTETUER<br>ADIPISCING ELIT. PRAESENT</p></div>
  <div class="abs btn-tan" style="left:308px;top:510px;width:91px;height:19px;font-size:10.5px">SHOP NOW</div>
</section>

<div class="abs rule" style="top:551px"></div>

<section class="featured">
  <h2 class="abs section-title" style="top:575px">FEATURED PRODUCTS</h2>
  <div class="abs card" style="left:74px;width:121px"><div class="item" role="img" aria-label="Silver vape mod"></div><div class="price">$ 120</div><div class="pname">PRODUCT NAME</div><div class="add">ADD TO CART</div></div>
  <div class="abs card" style="left:223px;width:121px"><div class="item" role="img" aria-label="Silver vape mod"></div><div class="price">$ 120</div><div class="pname">PRODUCT NAME</div><div class="add">ADD TO CART</div></div>
  <div class="abs card" style="left:365px;width:123px"><div class="item" role="img" aria-label="Silver vape mod"></div><div class="price">$ 120</div><div class="pname">PRODUCT NAME</div><div class="add">ADD TO CART</div></div>
  <div class="abs card" style="left:518px;width:119px"><div class="item" role="img" aria-label="Silver vape mod"></div><div class="price">$ 120</div><div class="pname">PRODUCT NAME</div><div class="add">ADD TO CART</div></div>
  <div class="abs btn-tan" style="left:266px;top:889px;width:181px;height:18px;font-size:10.5px">BROWSE MORE PRODUCTS</div>
</section>

<footer>
  <div class="abs footer"></div>
  <div class="abs follow"><h4>FOLLOW OUR UPDATES !</h4><p>Be the First to know about our Fresh Arrivals and much more!</p></div>
  <div class="abs subscribe"><div class="field">Enter Your Email</div><div class="send">SUBSCRIBE</div></div>

  <div class="abs links" style="left:62px"><h5>INFORMATION</h5><ul><li>About Us</li><li>Delivery Information</li><li>Privacy Policy</li><li>Terms &amp; Conditions</li><li>Contact Us</li></ul></div>
  <div class="abs links" style="left:208px"><h5>SERVICES</h5><ul><li>Returns</li><li>Site Map</li><li>Wish List</li><li>My Account</li><li>Order History</li></ul></div>
  <div class="abs links" style="left:354px"><h5>EXTRAS</h5><ul><li>Brands</li><li>Gift Certificates</li><li>Affiliates</li><li>Specials</li><li>Newsletter</li></ul></div>
  <div class="abs links" style="left:499px"><h5>CONTACTS</h5><ul><li>Warehouse &amp; Offices,</li><li>48 Harbour Lane, Napier NZ</li><li>(+064) 321 777</li><li>hello@coppermists.co</li><li>www.coppermists.co</li></ul></div>

  <div class="abs bottom">
    <div class="abs social"><span></span><span></span><span></span><span></span><span></span></div>
    <div class="abs copyright">COPYRIGHT 2019 © COPPER AND SLATE MISTS NZ</div>
    <div class="abs payments"><span></span><span></span><span></span><span></span><span></span></div>
  </div>
</footer>
</body>
</html>
```